Flyer für Immobilien (A4)
Zielgruppe
Es geht um den Verkauf von 2 Immobilien, welche auf diesem Flyer (DIN A4) mit Bildmateriel und kurzem Beschreib vorgestellt werden sollten.
Der Flyer ist für die Verteilung in Briefkästen von Privathaushältern gedacht.
Aufgabenstellung
Auf der Vorderseite sämtliche Texte, das Logo sowie die Aussenansicht der Liegenschaft (Bild 1) platzieren.
Auf der Rückseite können die restlichen Fotos in einer sinnvollen Aufteilung abgebildet werden.
Folgender Text sollte auf der Vorderseite gut aufgeteilt werden:
2x attraktive 4½-Zimmer-Wohnungen mit Balkon und schöner Aussicht ab Fr. 840‘000.—

```html
<!DOCTYPE html>
<html lang="de">
<head>
<meta charset="utf-8">
<title>Flyer Immobilien – Vorder- und Rückseite</title>
<link rel="stylesheet" href="https://fonts.googleapis.com/css2?family=Open+Sans:wght@300;400;600&display=swap">
<style>
  :root{
    --stage:#454446;
    --paper:#ffffff;
    --magenta:#a6095a;
    --ink:#2d2c2f;
    --white:#ffffff;
    --sky:#8fb0e6;
    --meadow:#7f9a3c;
    --interior:#e9e3d8;
    --floor:#c4a46a;
  }
  *{box-sizing:border-box;margin:0;padding:0}
  html,body{width:770px;height:1200px;overflow:hidden}
  body{background:var(--stage);font-family:"Open Sans",Arial,sans-serif;color:var(--white);position:relative}
  .page{position:absolute;left:185px;width:400px;height:566px;background:var(--paper);box-shadow:0 6px 18px rgba(0,0,0,.35)}
  .page--front{top:20px}
  .page--back{top:614px}
  .page__inner{position:absolute;inset:10px;}
  .block{position:absolute}
  .photo{position:absolute}
  /* Front */
  .photo--exterior{left:0;top:0;width:380px;height:425px;
    background:linear-gradient(160deg,var(--sky) 0%,#b7cdef 38%,#e8e0c8 50%,#a9b46a 66%,var(--meadow) 100%);
    clip-path:polygon(0 0,100% 0,100% 316px,130px 316px,130px 100%,0 100%)}
  .logo{position:absolute;right:8px;top:0;width:92px;height:56px;background:var(--paper);display:flex;align-items:center;justify-content:center;gap:5px;padding:0 6px}
  .logo__dot{width:9px;height:9px;border-radius:50%;background:var(--magenta);flex:none}
  .logo__name{font-size:8.5px;font-weight:600;color:var(--magenta);line-height:1.15}
  .panel--offer{left:136px;top:322px;width:244px;height:224px;background:var(--magenta);padding:13px 16px}
  .headline{font-weight:300;font-size:22px;line-height:1.08;letter-spacing:-.2px}
  .features{list-style:none;margin-top:6px}
  .features li{display:flex;align-items:center;gap:5px;font-weight:300;font-size:13px;line-height:1.3;white-space:nowrap}
  .tick{width:10px;height:10px;flex:none}
  .price-badge{position:absolute;left:28px;top:132px;width:82px;height:82px;border-radius:50%;background:var(--ink);border:1.5px solid var(--white);box-shadow:0 0 0 2px var(--ink);display:flex;flex-direction:column;align-items:center;justify-content:center;text-align:center;font-weight:300;line-height:1.15}
  .price-badge__from{font-size:8.5px}
  .price-badge__amount{font-size:12px;white-space:nowrap}
  .price-badge__meta{font-size:8px}
  .location{position:absolute;right:12px;bottom:12px;display:flex;align-items:flex-start;gap:5px;font-size:7.6px;font-weight:300;line-height:1.3;width:116px}
  .location span{white-space:nowrap}
  .location svg{width:10px;height:13px;flex:none}
  .panel--contact{left:0;top:431px;width:130px;height:115px;background:var(--ink);padding:10px 10px;font-size:7.6px;font-weight:300;line-height:1.4}
  .contact__lead{display:flex;gap:5px;align-items:flex-start;margin-bottom:4px}
  .contact__lead svg{width:12px;height:12px;flex:none}
  .contact__row{display:flex;align-items:center;gap:4px}
  .contact__row svg{width:8px;height:8px;flex:none}
  /* Back */
  .photo--living{left:0;top:0;width:140px;height:250px;background:linear-gradient(170deg,#f4f1ec 0%,var(--interior) 55%,var(--floor) 100%)}
  .photo--room{left:146px;top:0;width:234px;height:250px;background:linear-gradient(165deg,#f6f4f0 0%,#ebe6dc 50%,#cdb07a 100%)}
  .photo--bedroom{left:234px;top:256px;width:146px;height:260px;background:linear-gradient(160deg,#f5f3ef 0%,#dcdcdc 55%,#9aaab8 100%)}
  .panel--plan{left:0;top:256px;width:228px;height:260px;background:var(--magenta);padding:14px 12px}
  .floorplan{position:absolute;left:12px;top:18px;width:118px;height:150px;background:var(--ink);border:1.5px solid var(--white)}
  .facts{position:absolute;left:138px;top:18px;list-style:none}
  .facts li{display:flex;align-items:center;gap:4px;font-size:7.6px;font-weight:300;line-height:1.55;white-space:nowrap}
  .facts .tick{width:7px;height:7px}
  .footer{left:0;top:522px;width:380px;height:24px;background:var(--ink);display:flex;align-items:center;justify-content:space-between;gap:6px;padding:0 7px;font-size:5.4px;font-weight:300;white-space:nowrap}
</style>
</head>
<body>
<svg width="0" height="0" style="position:absolute" aria-hidden="true">
  <defs>
    <symbol id="icon-tick" viewBox="0 0 10 10"><circle cx="5" cy="5" r="5" fill="#fff"/><path d="M2.6 5.1l1.6 1.6 3.2-3.4" fill="none" stroke="#a6095a" stroke-width="1.4"/></symbol>
  </defs>
</svg>

<section class="page page--front" aria-label="Vorderseite">
  <div class="page__inner">
    <div class="photo photo--exterior" role="img" aria-label="Foto: Aussenansicht des Mehrfamilienhauses mit Balkonen, Obstbaum und Wiese unter blauem Himmel"></div>
    <div class="logo"><span class="logo__dot"></span><span class="logo__name">Lindenau &amp; Partner AG</span></div>

    <div class="block panel--offer">
      <h1 class="headline">2x attraktive<br>4½-Zimmer-<br>Wohnungen</h1>
      <ul class="features">
        <li><svg class="tick"><use href="#icon-tick"/></svg>mit Balkon</li>
        <li><svg class="tick"><use href="#icon-tick"/></svg>schöne Aussicht</li>
      </ul>
      <div class="price-badge">
        <span class="price-badge__from">ab</span>
        <span class="price-badge__amount">Fr. 840'000.–</span>
        <span class="price-badge__meta">4.5 Zimmer</span>
        <span class="price-badge__meta">112 m²</span>
      </div>
      <p class="location">
        <svg viewBox="0 0 10 13"><path d="M5 0a5 5 0 0 0-5 5c0 3.6 5 8 5 8s5-4.4 5-8a5 5 0 0 0-5-5z" fill="#fff"/><circle cx="5" cy="5" r="1.8" fill="#a6095a"/></svg>
        <span>Liegenschaft:<br>Mattenweg 5, 6300 Talbach</span>
      </p>
    </div>

    <div class="block panel--contact">
      <p class="contact__lead">
        <svg viewBox="0 0 12 12"><circle cx="6" cy="6" r="6" fill="#fff"/><rect x="5.2" y="5" width="1.6" height="4.2" fill="#2d2c2f"/><circle cx="6" cy="3.4" r=".9" fill="#2d2c2f"/></svg>
        <span>Detaillierte Verkaufsunterlagen oder Besichtigungen:</span>
      </p>
      <p>Lindenau &amp; Partner AG</p>
      <p class="contact__row"><svg viewBox="0 0 8 8"><circle cx="4" cy="4" r="3.4" fill="none" stroke="#fff" stroke-width="1"/><path d="M2.6 2.4l1 1.4-.5.6 1.2 1.2.6-.5 1.4 1" fill="none" stroke="#fff" stroke-width=".8"/></svg>041 555 20 17</p>
      <p class="contact__row"><svg viewBox="0 0 8 8"><rect x=".5" y="1.5" width="7" height="5" fill="none" stroke="#fff" stroke-width=".9"/><path d="M.5 1.8L4 4.6l3.5-2.8" fill="none" stroke="#fff" stroke-width=".9"/></svg>info@lindenau-partner.ch</p>
    </div>
  </div>
</section>

<section class="page page--back" aria-label="Rückseite">
  <div class="page__inner">
    <div class="photo photo--living" role="img" aria-label="Foto: Wohnzimmer mit Sofa und Parkettboden"></div>
    <div class="photo photo--room" role="img" aria-label="Foto: heller Wohnraum mit offener Küche"></div>

    <div class="block panel--plan">
      <div class="floorplan" role="img" aria-label="Grundriss der 4½-Zimmer-Wohnung mit Balkon"></div>
      <ul class="facts">
        <li><svg class="tick"><use href="#icon-tick"/></svg>4.5 Zimmer</li>
        <li><svg class="tick"><use href="#icon-tick"/></svg>112 m² Wohnfläche</li>
        <li><svg class="tick"><use href="#icon-tick"/></svg>Baujahr 1990</li>
        <li><svg class="tick"><use href="#icon-tick"/></svg>Zustand gut</li>
        <li><svg class="tick"><use href="#icon-tick"/></svg>Abstellkammer</li>
        <li><svg class="tick"><use href="#icon-tick"/></svg>Reduit</li>
        <li><svg class="tick"><use href="#icon-tick"/></svg>Bad/Dusche, 2 WC</li>
        <li><svg class="tick"><use href="#icon-tick"/></svg>Lift</li>
        <li><svg class="tick"><use href="#icon-tick"/></svg>Kellerabteil</li>
        <li><svg class="tick"><use href="#icon-tick"/></svg>Parkettböden</li>
        <li><svg class="tick"><use href="#icon-tick"/></svg>Bodenheizung</li>
        <li><svg class="tick"><use href="#icon-tick"/></svg>Gartenanteil</li>
        <li><svg class="tick"><use href="#icon-tick"/></svg>Einzelgarage</li>
      </ul>
    </div>
    <div class="photo photo--bedroom" role="img" aria-label="Foto: Schlafzimmer mit Bett und Wandbild"></div>

    <div class="block footer">
      <span>Kontakt: Lindenau &amp; Partner AG | Seestrasse 14 | 6300 Talbach | Tel. 041 555 20 17 | info@lindenau-partner.ch</span>
      <span>www.lindenau-partner.ch</span>
    </div>
  </div>
</section>
</body>
</html>
```